Business Cards

We were billed for this because the project timed out. Please give me another designed to open this back up. I was not happy with the last designs (that I was charged for).
we are also using the logo with Revitalizing Pools One Drop at a Time
Also want to utilize Where Healthy Water is our Commitment.

Contact Information for Business Card

Marlowe Stone Group Inc

```html
<!DOCTYPE html>
<html lang="en">
<head>
<meta charset="utf-8">
<title>Marlowe Stone Group Inc — Business Card</title>
<link rel="stylesheet" href="https://fonts.googleapis.com/css2?family=Montserrat:wght@400;500;700;800&display=swap">
<style>
  :root {
    --backdrop: #d3d4cf;
    --card-white: #ffffff;
    --card-dark: #3b3b3c;
    --pattern-dark: #2a2a2b;
    --pattern-light: #5a5a5c;
    --brand-blue: #1f74c2;
    --ink: #3a3a3a;
    --ink-soft: #555555;
  }
  * { box-sizing: border-box; margin: 0; padding: 0; }
  html, body {
    width: 1200px; height: 801px; overflow: hidden;
    background: var(--backdrop);
    font-family: "Montserrat", sans-serif;
  }
  .stage {
    position: relative; width: 1200px; height: 801px;
    display: flex; align-items: center; justify-content: center; gap: 50px;
  }
  .card {
    position: relative; width: 525px; height: 300px;
    border-bottom: 5px solid var(--brand-blue);
    box-shadow: 0 14px 30px rgba(0,0,0,0.18);
  }
  /* Front */
  .card-front { background: var(--card-white); }
  .brand-lockup {
    position: absolute; left: 34px; top: 150px; width: 230px;
  }
  .brand-name {
    font-weight: 800; font-size: 17px; letter-spacing: 0.5px;
    color: var(--ink); text-transform: uppercase; line-height: 1.1;
  }
  .brand-tagline {
    margin-top: 5px; font-size: 7.6px; letter-spacing: 1.1px;
    color: var(--ink-soft); text-transform: uppercase;
  }
  .contact-block {
    position: absolute; left: 290px; top: 56px; width: 220px;
    color: var(--ink);
  }
  .person-name {
    font-size: 21px; font-weight: 500; color: var(--brand-blue);
    text-transform: uppercase; letter-spacing: 0.2px;
  }
  .person-name .surname { font-weight: 700; }
  .person-role { font-size: 11px; margin-top: 2px; }
  .divider {
    width: 26px; height: 2px; background: var(--brand-blue);
    margin: 14px 0 12px;
  }
  .address { font-size: 11px; line-height: 1.45; }
  .contact-list { list-style: none; font-size: 11px; line-height: 1.55; }
  .contact-list li { display: flex; align-items: center; gap: 6px; }
  .contact-list svg { width: 9px; height: 9px; flex: none; }
  .contact-list .web-domain { color: var(--brand-blue); }
  /* Back */
  .card-back { background: var(--card-dark); overflow: hidden; }
  .back-pattern {
    position: absolute; inset: 0;
    background: linear-gradient(160deg, var(--pattern-light) 0%, var(--card-dark) 50%, var(--pattern-dark) 100%);
  }
  .back-brand {
    position: absolute; right: 30px; bottom: 40px;
    font-weight: 800; font-size: 15px; letter-spacing: 0.5px;
    color: var(--brand-blue); text-transform: uppercase;
  }
</style>
</head>
<body>
<main class="stage">
  <section class="card card-front" aria-label="Business card front">
    <div class="brand-lockup">
      <p class="brand-name">Marlowe Stone Group</p>
      <p class="brand-tagline">Revitalizing Pools One Drop at a Time</p>
    </div>
    <div class="contact-block">
      <p class="person-name">Dana <span class="surname">Whitfield</span></p>
      <p class="person-role">Managing Director</p>
      <div class="divider"></div>
      <p class="address">1187 Cedar Run Lane<br>Salem, OR 97301</p>
      <div class="divider"></div>
      <ul class="contact-list">
        <li>
          <svg viewBox="0 0 10 10" aria-hidden="true"><path d="M2 1 L4 1 L4.6 3 L3.4 3.8 Q4.4 5.8 6.2 6.6 L7 5.4 L9 6 L9 8 Q8.5 9 7.5 9 Q1 8 1 2.5 Q1 1 2 1Z" fill="var(--brand-blue)"/></svg>
          +945-555-0147
        </li>
        <li>
          <svg viewBox="0 0 10 10" aria-hidden="true"><rect x="0.8" y="2" width="8.4" height="6" fill="none" stroke="var(--brand-blue)" stroke-width="1"/><path d="M1 2.3 L5 5.5 L9 2.3" fill="none" stroke="var(--brand-blue)" stroke-width="1"/></svg>
          info@marlowestonegroup.com
        </li>
        <li>
          <svg viewBox="0 0 10 10" aria-hidden="true"><circle cx="5" cy="5" r="4.2" fill="none" stroke="var(--brand-blue)" stroke-width="1"/><ellipse cx="5" cy="5" rx="1.8" ry="4.2" fill="none" stroke="var(--brand-blue)" stroke-width="0.8"/><line x1="0.8" y1="5" x2="9.2" y2="5" stroke="var(--brand-blue)" stroke-width="0.8"/></svg>
          www.<span class="web-domain">marlowestonegroup.com</span>
        </li>
      </ul>
    </div>
  </section>

  <section class="card card-back" aria-label="Business card back">
    <div class="back-pattern" role="img" aria-label="Tone-on-tone repeating pattern of the company mark in dark grey gloss"></div>
    <p class="back-brand">Marlowe Stone Group</p>
  </section>
</main>
</body>
</html>
```